WordPress Site That Reviews Footwear

We need a wordpress web design for an affiliate site called TarnWisp. We review and do roundups on footwear products. The final design should be clean and mobile friendly. The site should be built with Gutenberg page builder. We like the design of https://petalharvin.com/.

Target Market(s)

USA

Industry/Entity Type

Footwear

Logo Text

TarnWisp

Number of Pages Required

4 page

Font styles to use
Serif
Sans Serif

Requirements
Must have
• Wordpress site
Blog post
Page
Categories
Homepage

```html
<!DOCTYPE html>
<html lang="en">
<head>
<meta charset="utf-8">
<title>TarnWisp – Footwear Reviews</title>
<link href="https://fonts.googleapis.com/css2?family=Montserrat:wght@500;600;700&family=Roboto:wght@400;500;700&display=swap" rel="stylesheet">
<style>
:root{
  --orange:#ea5a24;
  --navy:#10294a;
  --ink:#222;
  --text:#666;
  --grey:#f3f3f3;
  --white:#fff;
  --footer:#0f2944;
}
*{margin:0;padding:0;box-sizing:border-box}
html,body{width:1200px;height:3871px;overflow:hidden}
body{position:relative;background:var(--white);font-family:'Roboto',sans-serif;color:var(--text)}
.abs{position:absolute}
.photo{position:absolute}
.label{font-family:'Montserrat',sans-serif;font-weight:700;font-size:18px;color:var(--orange);letter-spacing:.3px}
.heading{font-family:'Montserrat',sans-serif;font-weight:500;font-size:29px;color:var(--navy);line-height:32px}
.rule{position:absolute;height:3px;width:94px;background:var(--orange)}
.para{font-size:14px;line-height:24px;text-align:justify;color:var(--text)}
.btn{position:absolute;background:var(--orange);color:var(--white);font-weight:700;font-size:15px;display:flex;align-items:center;justify-content:center}
.center{left:0;width:1200px;text-align:center}

.topbar{top:14px;left:111px;color:var(--white);font-size:15px;font-weight:500;display:flex;align-items:center;gap:14px}
.social-top{top:17px;right:108px;display:flex;gap:10px}
.social-top span{width:12px;height:12px;background:var(--white);border-radius:2px}
.social-top span:first-child{background:var(--orange)}
.nav{top:50px;left:111px;width:976px;height:67px;background:var(--white);display:flex;align-items:center;justify-content:space-between;padding:0 32px 0 33px}
.logo{font-family:'Montserrat',sans-serif;font-weight:700;font-size:33px;color:var(--orange)}
.nav ul{list-style:none;display:flex;gap:23px;font-size:15px;font-weight:500;color:var(--navy)}
.nav li:first-child{color:var(--orange)}
.hero-box{top:260px;left:308px;width:583px;height:194px;background:rgba(255,255,255,.85);text-align:center}
.hero-box h1{font-family:'Montserrat',sans-serif;font-weight:700;font-size:37px;color:var(--navy);margin-top:20px}
.hero-box h1 span{color:var(--orange)}
.hero-box p{font-size:20px;color:var(--ink);margin-top:8px}

.card{position:absolute;width:215px;height:190px;background:var(--white);box-shadow:0 2px 10px rgba(0,0,0,.12);text-align:center}
.card svg{margin-top:38px}
.card h3{font-family:'Montserrat',sans-serif;font-weight:600;font-size:18px;color:var(--navy);margin-top:18px}

.post{position:absolute;top:3092px;width:311px;height:358px;background:var(--white);box-shadow:0 2px 10px rgba(0,0,0,.13)}
.post .thumb{position:absolute;top:7px;left:7px;width:297px;height:206px}
.post .date{position:absolute;top:233px;left:17px;font-size:15px;color:var(--text);display:flex;align-items:center;gap:12px}
.post h4{position:absolute;top:266px;left:17px;width:290px;font-family:'Roboto',sans-serif;font-weight:500;font-size:18px;line-height:26px;color:var(--navy);white-space:nowrap}
.post .more{position:absolute;top:322px;left:17px;font-size:15px;font-weight:700;color:var(--orange);display:flex;align-items:center;gap:12px}

.footer{top:3546px;left:0;width:1200px;height:325px;background:var(--footer);color:var(--white)}
.fcol{position:absolute;top:52px}
.fcol h5{font-family:'Montserrat',sans-serif;font-weight:600;font-size:19px;margin-bottom:18px}
.fcol h5::after{content:"";display:block;width:44px;height:3px;background:var(--orange);margin-top:8px}
.fcol li{list-style:none;font-size:15px;line-height:25.5px;display:flex;align-items:flex-start;gap:22px}
.dot{width:12px;height:12px;border:2px solid var(--orange);border-radius:50%;margin-top:7px;flex:none}
.fsocial{position:absolute;top:105px;left:892px;display:flex;gap:10px}
.fsocial span{width:36px;height:37px;border:1px solid rgba(255,255,255,.6);display:flex;align-items:center;justify-content:center}
.fsocial span::after{content:"";width:10px;height:10px;background:var(--orange)}
.copy{position:absolute;top:283px;left:0;width:1200px;text-align:center;font-size:12px}
.copy span{color:var(--orange)}
</style>
</head>
<body>

<div class="photo" style="top:0;left:0;width:1200px;height:625px;background:linear-gradient(135deg,#3a3a35 0%,#c9553c 35%,#7b6a5c 60%,#4a4d4f 100%)" role="img" aria-label="Runner in red shoes tying laces on asphalt"></div>
<div class="abs topbar">
  <svg width="12" height="12" viewBox="0 0 12 12"><path d="M2 1l2 0 1 3-1.5 1a7 7 0 003.5 3.5L8 7l3 1v2c0 1-1 1-1 1A10 10 0 011 2s0-1 1-1z" fill="#ea5a24"/></svg>
  <span>555-218-4390</span><span>|</span>
  <svg width="14" height="11" viewBox="0 0 14 11"><rect width="14" height="11" rx="1" fill="#ea5a24"/><path d="M0 1l7 5 7-5" stroke="#fff" fill="none"/></svg>
  <span>info@tarnwisp.com</span>
</div>
<div class="abs social-top"><span></span><span></span><span></span><span></span></div>
<nav class="abs nav">
  <div class="logo">TarnWisp</div>
  <ul><li>Home</li><li>About Us</li><li>Our Benefits</li><li>Why Choose Us</li><li>Our Resources</li><li>Contact us</li></ul>
</nav>
<div class="abs hero-box">
  <h1>WELCOME TO <span>TARNWISP</span></h1>
  <p>Lorem ipsum dolor sit amet consectetua</p>
</div>
<div class="btn" style="top:386px;left:532px;width:136px;height:46px;font-size:14px">GET STARTED</div>

<div class="abs label" style="top:714px;left:111px">WHY CHOOSE US</div>
<div class="abs heading" style="top:748px;left:111px;width:440px">Lorem ipsum dolor sit amet consectetur adipia</div>
<div class="rule" style="top:823px;left:111px"></div>
<div class="abs para" style="top:856px;left:111px;width:476px">Lorem ipsum dolor sit amet, consectetur adipiscing elit, sed do eiusmod tempor incididunt ut labore et dolore magna aliqua. Ut enim ad minim veniam, quis nostrud exercitation ullamco laboris nisi ut aliquip ex ea commodo consequau dutis aute irure dolor.</div>
<div class="abs para" style="top:966px;left:111px;width:476px">Sed ut perspiciatis unde omnis iste natus error sit voluptatem accus antium doloremque laudantium, totam rem aperiam, eaque ipsa qua e ab illo inventore veritatis et quasi architecto.</div>
<div class="btn" style="top:1072px;left:111px;width:138px;height:49px">LEARN MORE</div>

<div class="card" style="top:719px;left:634px">
  <svg width="62" height="62" viewBox="0 0 62 62" fill="none" stroke="#10294a" stroke-width="2"><circle cx="31" cy="22" r="13" stroke="#ea5a24"/><path d="M8 60V44M16 60V40M24 60V46M32 60V42M40 60V38M48 60V34M56 60V28M44 10l12-6-2 12" /></svg>
  <h3>PERSPICIATIS</h3>
</div>
<div class="card" style="top:719px;left:871px">
  <svg width="62" height="62" viewBox="0 0 62 62" fill="none" stroke="#10294a" stroke-width="2"><path d="M6 52h50M14 44h42M20 36l26 0" /><path d="M4 40h10M2 48h8" stroke="#ea5a24"/></svg>
  <h3>PERSPICIATIS</h3>
</div>
<div class="card" style="top:930px;left:634px">
  <svg width="62" height="62" viewBox="0 0 62 62" fill="none" stroke="#10294a" stroke-width="2"><path d="M31 28C20 20 20 8 26 6c3-1 5 1 5 3 0-2 2-4 5-3 6 2 6 14-5 22z" stroke="#ea5a24"/><path d="M6 28l4 16 10 10v6M56 28l-4 16-10 10v6"/></svg>
  <h3>PERSPICIATIS</h3>
</div>
<div class="card" style="top:930px;left:871px">
  <svg width="62" height="62" viewBox="0 0 62 62" fill="none" stroke="#10294a" stroke-width="2"><circle cx="31" cy="26" r="20"/><circle cx="31" cy="26" r="13" stroke="#ea5a24"/><path d="M25 26l4 4 8-8" stroke="#ea5a24"/><path d="M20 42l-6 16 8-4 4 6 5-14M42 42l6 16-8-4-4 6-5-14"/></svg>
  <h3>PERSPICIATIS</h3>
</div>

<div class="photo" style="top:1218px;left:0;width:428px;height:470px;background:linear-gradient(120deg,#2f2a26 0%,#8a6e5c 45%,#8fb3d4 75%,#3b3533 100%)" role="img" aria-label="Smiling woman trying on shoes in a store"></div>
<div class="abs" style="top:1218px;left:428px;width:772px;height:470px;background:var(--grey)"></div>
<div class="abs label" style="top:1257px;left:524px">ABOUT US</div>
<div class="abs heading" style="top:1289px;left:524px;width:560px">Lorem ipsum dolor sit amet consectetur adipia Sed ut perspicia</div>
<div class="rule" style="top:1364px;left:524px"></div>
<div class="abs para" style="top:1397px;left:524px;width:563px">Lorem ipsum dolor sit amet, consectetur adipiscing elit, sed do eiusmod tempor incididunt ut labore et dolore magna aliqua. Ut enim ad minim veniam, quis nostrud exercitation ullamco laboris nisi ut aliquip ex ea commodo consequat. Duis aute irure dolor in reprehenderit in voluptate velit esse cillum dolore. Sed ut perspiciatis unde omnis iste natus error sit voluptatem accusantium doloremque laudantium, totam rem aperiam, eaque ipsa quae ab illo inventore veritatis et quasi architecto beatae vitae dicta sunt explicabo laboris nisi ut aliquip ex ea commodo consequdo.</div>
<div class="btn" style="top:1600px;left:524px;width:138px;height:47px">LEARN MORE</div>

<div class="abs label center" style="top:1781px">FEATURED BENEFITS</div>
<div class="abs heading center" style="top:1812px">Lorem ipsum dolor sit amet consectetur adipia</div>
<div class="rule" style="top:1866px;left:553px"></div>
<div class="photo" style="top:1913px;left:111px;width:976px;height:471px;background:linear-gradient(110deg,#8d8c89 0%,#6d5546 35%,#a4683e 60%,#b9b6b0 100%)" role="img" aria-label="Person in sneakers sitting on a street bench with a leather bag"></div>
<svg class="abs" style="top:2088px;left:539px" width="120" height="120" viewBox="0 0 120 120"><circle cx="60" cy="60" r="58" fill="none" stroke="#ea5a24" stroke-width="2"/><circle cx="60" cy="60" r="40" fill="#ea5a24"/><path d="M52 46l22 14-22 14z" fill="#fff"/></svg>

<div class="abs" style="top:2480px;left:0;width:770px;height:389px;background:var(--orange)"></div>
<div class="photo" style="top:2480px;left:770px;width:430px;height:389px;background:linear-gradient(120deg,#3a3936 0%,#b8bcc7 45%,#dfe3ea 70%,#6c5a4c 100%)" role="img" aria-label="Smiling man in glasses holding a brown leather shoe in a shop"></div>
<div class="abs label" style="top:2523px;left:111px;color:var(--white)">TESTIMONIALS</div>
<div class="abs heading" style="top:2555px;left:111px;color:var(--white)">What About Our Clients Say</div>
<div class="rule" style="top:2602px;left:111px;background:var(--white)"></div>
<div class="abs" style="top:2490px;left:515px;font-family:'Montserrat',sans-serif;font-weight:700;font-size:260px;line-height:260px;color:rgba(255,255,255,.22)">”</div>
<div class="abs para" style="top:2635px;left:111px;width:563px;color:var(--white)">“Sed ut perspiciatis unde omnis iste natus error sit voluptatem accusantium doloremque laudantium, totam rem aperiam, eaque ipsa quae ab illo inventore veritatis et quasi architecto beatae vitae dicta sunt explicabo. Nemo enim ipsum voluptatem quia voluptas sit aspernatur aut odit aut fugit, sed quia consequuntur magni dolores eos qui ratione voluptatem sequi nesciunt.”</div>
<div class="abs" style="top:2780px;left:111px;color:var(--white);font-size:20px;font-weight:700">JOHN SMITH, <span style="font-size:15px;font-weight:400">United States</span></div>
<div class="abs" style="top:2809px;left:111px;color:var(--white);font-size:15px;letter-spacing:1px">★★★★★</div>
<div class="abs" style="top:2834px;left:734px;width:36px;height:35px;background:var(--white);display:flex;align-items:center;justify-content:center"><svg width="10" height="14"><path d="M8 1L2 7l6 6" stroke="#ea5a24" stroke-width="3" fill="none"/></svg></div>
<div class="abs" style="top:2834px;left:770px;width:37px;height:35px;background:var(--orange);display:flex;align-items:center;justify-content:center"><svg width="10" height="14"><path d="M2 1l6 6-6 6" stroke="#fff" stroke-width="3" fill="none"/></svg></div>

<div class="abs label center" style="top:2963px">OUR RESOURCES</div>
<div class="abs heading center" style="top:2994px">Lorem ipsum dolor sit amet consectetur adipia</div>
<div class="rule" style="top:3047px;left:553px"></div>

<div class="post" style="left:111px">
  <div class="thumb" style="background:linear-gradient(160deg,#bfc6cc,#e4ddd4 55%,#8a8f92)" role="img" aria-label="Sneakers on a skateboard"></div>
  <div class="date"><svg width="14" height="14"><rect x="1" y="2" width="12" height="11" fill="none" stroke="#ea5a24" stroke-width="1.5"/><path d="M1 6h12" stroke="#ea5a24"/></svg>05 Jul 2021</div>
  <h4>Lorem ipsum dolor sit ametcoa<br>nsectetur adipiscing</h4>
  <div class="more">READ MORE <span class="dot" style="margin:0"></span></div>
</div>
<div class="post" style="left:443px">
  <div class="thumb" style="background:linear-gradient(160deg,#a9a29b,#d8cbbd 55%,#8f8781)" role="img" aria-label="Woman in a cream outfit seated on the floor"></div>
  <div class="date"><svg width="14" height="14"><rect x="1" y="2" width="12" height="11" fill="none" stroke="#ea5a24" stroke-width="1.5"/><path d="M1 6h12" stroke="#ea5a24"/></svg>05 Jul 2021</div>
  <h4>Lorem ipsum dolor sit ametcoa<br>nsectetur adipiscing</h4>
  <div class="more">READ MORE <span class="dot" style="margin:0"></span></div>
</div>
<div class="post" style="left:775px">
  <div class="thumb" style="background:linear-gradient(170deg,#a8a7a4,#7b6254 55%,#3d3a36)" role="img" aria-label="Hiker in teal shoes standing on rocks"></div>
  <div class="date"><svg width="14" height="14"><rect x="1" y="2" width="12" height="11" fill="none" stroke="#ea5a24" stroke-width="1.5"/><path d="M1 6h12" stroke="#ea5a24"/></svg>05 Jul 2021</div>
  <h4>Lorem ipsum dolor sit ametcoa<br>nsectetur adipiscing</h4>
  <div class="more">READ MORE <span class="dot" style="margin:0"></span></div>
</div>

<footer class="abs footer">
  <div class="fcol" style="left:110px">
    <h5>Our Company</h5>
    <ul><li><span class="dot"></span>Home</li><li><span class="dot"></span>About Us</li><li><span class="dot"></span>Our Benefits</li><li><span class="dot"></span>Why Choose Us</li><li><span class="dot"></span>Our Resources</li></ul>
  </div>
  <div class="fcol" style="left:359px">
    <h5>Legal</h5>
    <ul><li><span class="dot"></span>Privacy Policy</li><li><span class="dot"></span>Terms Of Use</li><li><span class="dot"></span>Support</li></ul>
  </div>
  <div class="fcol" style="left:593px">
    <h5>Contact Us</h5>
    <ul>
      <li><svg width="12" height="16" style="margin-top:4px;flex:none"><path d="M6 15C2 9 1 7 1 5a5 5 0 0110 0c0 2-1 4-5 10z" fill="#ea5a24"/><circle cx="6" cy="5" r="2" fill="#0f2944"/></svg><span>72, Harlow Lane<br>Riverton</span></li>
      <li style="margin-top:8px"><svg width="12" height="12" style="margin-top:6px;flex:none"><path d="M2 1l2 0 1 3-1.5 1a7 7 0 003.5 3.5L8 7l3 1v2c0 1-1 1-1 1A10 10 0 011 2s0-1 1-1z" fill="#ea5a24"/></svg>555-218-4390</li>
      <li style="margin-top:8px"><svg width="13" height="10" style="margin-top:8px;flex:none"><rect width="13" height="10" fill="#ea5a24"/><path d="M0 1l6.5 5L13 1" stroke="#0f2944" fill="none"/></svg>info@tarnwisp.com</li>
    </ul>
  </div>
  <div class="abs logo" style="top:38px;left:870px;font-size:39px">TarnWisp</div>
  <div class="fsocial"><span></span><span></span><span></span><span></span></div>
  <div class="copy">© Copyrights 2021 TarnWisp. All Rights Reserved</div>
</footer>

</body>
</html>
```